Brightwell Audiology Centre - is state of the art audiology clinic and needs a business card design

the card should be oriented in 'portrait' mode and have a clinic logo. The card should be double sided, with logo on the front and my details on the other side of the card

We would also like to use a tagline of 'Experts in Hearing Care'

Clinic

```html
<!DOCTYPE html>
<html lang="en">
<head>
<meta charset="utf-8">
<title>Brightwell Audiology Centre – Business Card</title>
<link rel="stylesheet" href="https://fonts.googleapis.com/css2?family=Montserrat:wght@600&family=Arimo:wght@700&family=Cousine&display=swap">
<style>
  :root {
    --backdrop: #eef0f0;
    --card-dark: #0a0b0d;
    --card-blue: #268bfa;
    --accent-cyan: #7fe3f5;
    --text-light: #ffffff;
  }
  html, body {
    margin: 0;
    padding: 0;
    width: 1200px;
    height: 791px;
    overflow: hidden;
    background: var(--backdrop);
  }
  .canvas {
    position: relative;
    width: 1200px;
    height: 791px;
  }
  .card {
    position: absolute;
    top: 125px;
    width: 320px;
    height: 540px;
    overflow: hidden;
    color: var(--text-light);
  }
  .card--details {
    left: 260px;
    background: var(--card-dark);
  }
  .card--brand {
    left: 620px;
    background: var(--card-blue);
  }

  /* Details side */
  .brand-mark {
    position: absolute;
    left: 50%;
    top: 56px;
    width: 56px;
    height: 56px;
    margin-left: -28px;
    border-radius: 50%;
    background: var(--accent-cyan);
  }
  .brand-name {
    position: absolute;
    left: 0;
    right: 0;
    top: 140px;
    margin: 0;
    text-align: center;
    font-family: "Montserrat", sans-serif;
    font-weight: 600;
    font-size: 18px;
    line-height: 24px;
    letter-spacing: 0.5px;
    text-transform: uppercase;
  }
  .tagline {
    font-family: "Arimo", sans-serif;
    font-weight: 700;
  }
  .card--details .tagline {
    position: absolute;
    left: 0;
    right: 0;
    top: 196px;
    margin: 0;
    text-align: center;
    font-size: 14px;
  }
  .contact {
    font-family: "Cousine", monospace;
    font-size: 16px;
    line-height: 22px;
    margin: 0;
  }
  .contact-person {
    position: absolute;
    left: 28px;
    top: 318px;
  }
  .contact-office {
    position: absolute;
    left: 28px;
    top: 378px;
  }
  .contact-online {
    position: absolute;
    left: 0;
    right: 0;
    top: 462px;
    text-align: center;
    line-height: 23px;
  }

  /* Brand side */
  .brand-disc {
    position: absolute;
    left: -70px;
    top: 60px;
    width: 220px;
    height: 220px;
    border-radius: 50%;
    background: var(--text-light);
  }
  .brand-divider {
    position: absolute;
    left: 40px;
    top: 308px;
    width: 3px;
    height: 140px;
    background: var(--text-light);
  }
  .brand-stack {
    position: absolute;
    left: 64px;
    top: 316px;
    margin: 0;
    font-family: "Montserrat", sans-serif;
    font-weight: 600;
    font-size: 26px;
    line-height: 33px;
    letter-spacing: 0.5px;
    text-transform: uppercase;
  }
  .card--brand .tagline {
    position: absolute;
    left: 64px;
    top: 417px;
    margin: 0;
    font-size: 16px;
  }
</style>
</head>
<body>
<main class="canvas">
  <section class="card card--details">
    <div class="brand-mark"></div>
    <h1 class="brand-name">Brightwell<br>Audiology Centre</h1>
    <p class="tagline">Experts in Hearing Care</p>
    <p class="contact contact-person">Dr.Harlan<br>Audiology</p>
    <p class="contact contact-office">phone:555.210.4478<br>4816 , Alder street</p>
    <p class="contact contact-online">dr_bac@mail.com<br>www.bwac.com</p>
  </section>

  <section class="card card--brand">
    <div class="brand-disc"></div>
    <div class="brand-divider"></div>
    <h2 class="brand-stack">Brightwell<br>Audiology<br>Centre</h2>
    <p class="tagline">Experts in Hearing Care</p>
  </section>
</main>
</body>
</html>
```